TaleBeacons business card for creator of IP TOY (fun) (children) designs

This business card will be the introduction of me as the creator of new designs to the toy industry and beyond. These designs are kept secret until being revealed one on one to each company. My design is patent pending protected IP. I am looking for business appropriate with a tinge of fun. Please no black backgounds as this is the toy industry. Be creative with the logo and colors please. Just imagine.

Target Market(s)

TOY Industry Executives - Inventor Relations - Manufacturers this is my first introduction card.

Industry/Entity Type

Toy Industry - I have included our Brand colors which can be seen on the cover of The Tiny Blue Goat book so uses for any of these others colors would be intersting.

Contact Information for Business Card

LOGO Delia Vantreck Founder Creator 214 555 0182 2817 E Mallow Ridge Anna, TX 75288 www.talebeacons.example deliavantreck@mailhollow.example Patent Pending IP

Font styles to use
Other font styles liked:
• The font used in the logo is Swiss721BT bold I need to see other fonts to be able to decide but need a clean look

Requirements
Must have
• A bit of an artistic flair although the logo is very simple. I am in the toy industry so would like something that sparks the look of being a creator?
Nice to have
• Please try a background other than stark white. Would like to see a play using brand colors?I like the logos which look like they are lifted off the page. Then under the logo the words (not lifted?) Any Action Any Character Any Teaching
Should not have
• No Black Backgrounds please! should look as clean as possible - I am not opposed to changing to a double sided card if that is more effectual.

```html
<!DOCTYPE html>
<html lang="en">
<head>
<meta charset="utf-8">
<title>TaleBeacons Business Card</title>
<link href="https://fonts.googleapis.com/css2?family=Arimo:wght@700&family=Lato:wght@400;700&display=swap" rel="stylesheet">
<style>
  :root {
    --page-bg: #e6e6e6;
    --sky-top: #6fa9dc;
    --sky-bottom: #bfdaf2;
    --brand-red: #d8232a;
    --cream: #fbebd1;
    --band-blue: #6aa6dc;
    --band-yellow: #f5bf22;
    --fence-white: #ffffff;
    --sunflower: #f2a81d;
    --leaf: #3f8b3a;
    --house: #efd9a8;
    --roof: #c8312c;
    --ink: #222222;
  }
  * { box-sizing: border-box; margin: 0; padding: 0; }
  html, body { width: 1200px; height: 1000px; overflow: hidden; }
  body {
    background: var(--page-bg);
    position: relative;
    font-family: "Lato", Arial, sans-serif;
  }
  .card {
    position: absolute;
    left: 220px;
    width: 760px;
    height: 434px;
    overflow: hidden;
    box-shadow: 0 6px 18px rgba(0,0,0,0.12);
  }
  .card--front { top: 40px; background: linear-gradient(160deg, var(--sky-top) 0%, var(--sky-bottom) 70%); }
  .card--back { top: 526px; background: var(--cream); }

  .wordmark {
    position: absolute;
    font-family: "Arimo", Arial, sans-serif;
    font-weight: 700;
    color: var(--brand-red);
    white-space: nowrap;
  }
  .card--front .wordmark { left: 170px; top: 150px; font-size: 62px; }
  .site-url {
    position: absolute;
    left: 282px; top: 250px;
    font-size: 17px;
    letter-spacing: 3px;
    color: var(--ink);
  }
  .site-url .accent { color: var(--brand-red); }

  .art { position: absolute; }
  .art--bees { left: 430px; top: 70px; width: 110px; height: 52px; background: linear-gradient(90deg, #f3d23c, #e0463f); border-radius: 26px; }
  .art--fence { left: 0; bottom: 0; width: 760px; height: 96px; background: linear-gradient(180deg, rgba(255,255,255,0.75), var(--fence-white)); }
  .art--house { left: 40px; bottom: 50px; width: 180px; height: 120px; background: linear-gradient(180deg, var(--roof) 0 30%, var(--house) 30% 100%); }
  .art--sunflowers { right: 40px; bottom: 80px; width: 110px; height: 170px; background: linear-gradient(180deg, var(--sunflower) 0 70%, var(--leaf) 100%); border-radius: 40px 40px 10px 10px; }

  .card--back .wordmark { left: 70px; top: 210px; font-size: 50px; }
  .contact {
    position: absolute;
    left: 430px; top: 92px;
    color: var(--brand-red);
  }
  .contact__name { font-family: "Arimo", Arial, sans-serif; font-weight: 700; font-size: 30px; line-height: 1; }
  .contact__role { font-family: "Arimo", Arial, sans-serif; font-weight: 700; font-size: 16px; margin-top: 8px; letter-spacing: 0.5px; }
  .contact__rule { width: 96px; height: 2px; background: var(--brand-red); margin: 18px 0 16px; }
  .contact__list { list-style: none; font-size: 17px; line-height: 1.45; }
  .contact__list li { display: flex; align-items: flex-start; gap: 10px; }
  .contact__list svg { width: 16px; height: 16px; margin-top: 4px; flex: none; }
  .contact__list .indent { padding-left: 26px; }

  .art--bee-small { left: 36px; bottom: 34px; width: 60px; height: 46px; background: linear-gradient(90deg, #f3d23c, #e0463f); border-radius: 23px; }
  .band { position: absolute; bottom: 0; height: 14px; }
  .band--blue { left: 0; width: 520px; background: var(--band-blue); }
  .band--yellow { left: 520px; width: 240px; background: var(--band-yellow); }
</style>
</head>
<body>
  <section class="card card--front" aria-label="Card front">
    <div class="art art--bees" role="img" aria-label="Two striped cartoon bees flying"></div>
    <div class="wordmark">TaleBeacons</div>
    <p class="site-url">WWW.<span class="accent">TALEBEACONS</span>.EXAMPLE</p>
    <div class="art art--fence" role="img" aria-label="White picket fence along the bottom of the card"></div>
    <div class="art art--house" role="img" aria-label="Small house with red roof behind the fence"></div>
    <div class="art art--sunflowers" role="img" aria-label="Sunflowers with a bee growing by the fence"></div>
  </section>

  <section class="card card--back" aria-label="Card back">
    <div class="wordmark">TaleBeacons</div>
    <div class="contact">
      <h1 class="contact__name">DELIA VANTRECK</h1>
      <p class="contact__role">FOUNDER CREATOR</p>
      <div class="contact__rule"></div>
      <ul class="contact__list">
        <li>
          <svg viewBox="0 0 16 16" aria-hidden="true"><rect x="1" y="2" width="14" height="12" rx="2" fill="var(--band-blue)"/><rect x="4" y="5" width="8" height="2" fill="#fff"/><rect x="4" y="9" width="8" height="2" fill="#fff"/></svg>
          <span>214 555 0182</span>
        </li>
        <li>
          <svg viewBox="0 0 16 16" aria-hidden="true"><path d="M1 7 L15 1 L9 15 L7 9 Z" fill="var(--band-blue)"/></svg>
          <span>deliavantreck@mailhollow.example</span>
        </li>
        <li>
          <svg viewBox="0 0 16 16" aria-hidden="true"><path d="M8 1a5 5 0 0 0-5 5c0 4 5 9 5 9s5-5 5-9a5 5 0 0 0-5-5z" fill="var(--band-blue)"/><circle cx="8" cy="6" r="2" fill="#fff"/></svg>
          <span>2817 E Mallow Ridge</span>
        </li>
        <li class="indent"><span>Anna, TX 75288</span></li>
        <li>
          <svg viewBox="0 0 16 16" aria-hidden="true"><circle cx="8" cy="8" r="7" fill="var(--band-blue)"/><path d="M1 8h14M8 1c-3 4-3 10 0 14M8 1c3 4 3 10 0 14" stroke="#fff" stroke-width="1.2" fill="none"/></svg>
          <span>Patent Pending IP</span>
        </li>
      </ul>
    </div>
    <div class="art art--bee-small" role="img" aria-label="Small striped cartoon bee"></div>
    <div class="band band--blue"></div>
    <div class="band band--yellow"></div>
  </section>
</body>
</html>
```